Skin cancer clinic services trifold brochure

Need trifold brochure listing skin cancer services our clinic provides, staff information, location and brief about skin cancer with colours similar to our web site www.Lumorava.clinic. I will provide more information regarding services and staff but want this colourful and standout as it will be given to other referring doctors or patients

Target Market(s)

Age 40 to 80 years

Industry/Entity Type

Medical

Font styles to use
Serif

Colors

Designer to choose colors to be used in the design.

Requirements
Must have
• Logo, services, contact info, beach or sun look and colours similar to web site or logo

```html
<!DOCTYPE html>
<html lang="en">
<head>
<meta charset="utf-8">
<title>Lumorava Skin Cancer Clinic – Trifold Brochure</title>
<link rel="stylesheet" href="https://fonts.googleapis.com/css2?family=Lora:wght@400;700&family=Great+Vibes&display=swap">
<style>
:root{
  --bg:#6b6c70;
  --orange:#e3792b;
  --orange-deep:#d4520d;
  --orange-dot:#c9460c;
  --amber:#f0a530;
  --amber-light:#f6bd55;
  --ink:#3b2d22;
  --body:#333333;
  --white:#ffffff;
  --dusk-top:#e9b6a6;
  --dusk-mid:#c7998f;
  --dusk-low:#6f6c7a;
}
*{margin:0;padding:0;box-sizing:border-box}
html,body{width:1200px;height:1200px;overflow:hidden}
body{background:var(--bg);font-family:'Lora',Georgia,serif;position:relative}
.brochure{position:absolute;left:30px;top:171px;width:1140px;height:858px;display:flex;box-shadow:0 18px 30px rgba(0,0,0,.35)}
.panel{position:relative;height:100%;overflow:hidden}

/* About panel */
.panel-about{width:372px;background:var(--white)}
.about-title{position:absolute;left:25px;top:27px;font-size:25px;font-weight:700;color:var(--orange)}
.about-rule{position:absolute;left:151px;right:0;top:40px;height:8px;background:var(--orange)}
.band{position:absolute;left:0;right:0;background:var(--orange)}
.band-top{top:70px;height:12px}
.band-mid{top:281px;height:11px}
.band-foot{top:690px;height:15px}
.band-base{top:843px;height:15px;background:linear-gradient(90deg,var(--amber) 0 50%,var(--orange) 50% 100%)}
.photo-clinician{position:absolute;left:0;right:0;top:82px;height:199px;background:linear-gradient(120deg,#d9dadc 0%,#eef0f1 45%,#c9ced2 100%)}
.badge{position:absolute;left:23px;top:222px;width:100px;height:100px;border-radius:50%;background:var(--white);border:4px solid var(--amber)}
.about-copy{position:absolute;left:23px;top:340px;width:318px;font-size:13.4px;line-height:18.5px;color:var(--body);text-align:justify}
.about-copy p{margin-bottom:18.5px}
.about-copy p:last-child{margin-bottom:0}
.about-copy a{color:var(--orange);text-decoration:none}
.map{position:absolute;left:0;right:0;top:705px;height:138px;background:linear-gradient(135deg,#eceae6 0%,#f4f3f0 50%,#dfe6ea 100%)}
.map-marker{position:absolute;left:158px;top:27px;width:88px;height:88px;border-radius:50%;background:rgba(240,165,48,.55)}

/* Skin cancer panel */
.panel-info{width:384px;background:linear-gradient(180deg,var(--orange) 0 455px,var(--amber) 455px,var(--amber-light) 100%)}
.info-glow{position:absolute;left:0;right:0;top:0;height:455px;background:linear-gradient(90deg,rgba(255,255,255,0) 40%,rgba(180,70,10,.25) 100%)}
.dot{position:absolute;border-radius:50%;background:var(--orange-dot)}
.info-title{position:absolute;left:35px;top:21px;font-size:25px;font-weight:700;color:var(--ink)}
.info-kicker{position:absolute;left:35px;top:72px;font-size:14px;color:var(--ink)}
.info-copy{position:absolute;left:35px;top:110px;width:312px;font-size:13.1px;line-height:18.6px;color:var(--ink);text-align:justify}
.photo-frame{position:absolute;left:38px;top:332px;width:312px;height:315px;background:var(--amber)}
.photo-couple{position:absolute;left:49px;top:344px;width:300px;height:291px;background:linear-gradient(150deg,#b8a470 0%,#d7d2c8 40%,#4c5b66 75%,#8c3a2e 100%)}
.callout{position:absolute;left:28px;top:255px;width:162px;height:162px;border-radius:50%;background:rgba(212,82,13,.82);display:flex;align-items:center;justify-content:center;text-align:center;color:var(--white);font-size:22px;font-weight:700;line-height:30px}
.contact-title{position:absolute;left:70px;top:648px;font-size:19px;font-weight:400;color:var(--ink)}
.contact-list{position:absolute;left:48px;top:692px;list-style:none;font-size:15px;color:var(--ink);line-height:25.5px}
.contact-list li{display:flex;align-items:flex-start}
.contact-list svg{width:15px;height:15px;margin:5px 7px 0 0;flex:none}
.contact-list .indent{padding-left:22px}

/* Cover panel */
.panel-cover{width:384px;background:linear-gradient(180deg,var(--dusk-top) 0%,var(--dusk-mid) 50%,var(--dusk-low) 100%)}
.cover-photo{position:absolute;inset:0}
.cover-logo{position:absolute;left:0;right:0;top:228px;text-align:center;font-size:40px;color:var(--white)}
.cover-tagline{position:absolute;left:0;right:0;top:630px;text-align:center;font-family:'Great Vibes',cursive;font-size:48px;line-height:50px;color:var(--white)}
</style>
</head>
<body>
<div class="brochure">

  <section class="panel panel-about">
    <h2 class="about-title">About Us</h2>
    <div class="about-rule"></div>
    <div class="band band-top"></div>
    <div class="photo-clinician" role="img" aria-label="Photo of a clinician in mask and gloves inspecting a sample in a bright clinic"></div>
    <div class="band band-mid"></div>
    <div class="badge" role="img" aria-label="Accreditation badge"></div>
    <div class="about-copy">
      <p>Lumorava Skin Cancer Clinic is a purpose-built skin cancer clinic dedicated to providing the higest-level patient care to the Central Coast community and surrounding regions.</p>
      <p>Our skilled doctors and nurses have extensive experience and advanced training in Skin Cancer Medicine in order to provide quality care to our patients. We specialise in a comprehensive approach to skin with preventive skin cancer care, expert diagnostic dermoscopy skills highlighting artificial intelligent analytics, and definitive surgical and medical treatments of skin cancers.</p>
      <p>Skin cancer medicine is all we do.</p>
      <p>We welcome you to “virtually” walk through our clinic at <a href="#">www.Lumorava.clinic</a></p>
    </div>
    <div class="band band-foot"></div>
    <div class="map" role="img" aria-label="Street map showing the clinic location">
      <div class="map-marker"></div>
    </div>
    <div class="band band-base"></div>
  </section>

  <section class="panel panel-info">
    <div class="info-glow"></div>
    <div class="dot" style="left:230px;top:3px;width:72px;height:72px"></div>
    <div class="dot" style="left:325px;top:37px;width:28px;height:28px"></div>
    <div class="dot" style="left:318px;top:86px;width:40px;height:40px"></div>
    <div class="dot" style="left:210px;top:269px;width:72px;height:72px"></div>
    <div class="dot" style="left:304px;top:302px;width:28px;height:28px"></div>
    <h2 class="info-title">Skin Cancer</h2>
    <p class="info-kicker">Did you know?</p>
    <p class="info-copy">Skin Cancers account for 80% of all newly diagnosed cancers with two in three Australians diagnosed with skin cancer by the time they are 70. Although over 90% of skin cancers are due to over exposure to UV light, some are caused by chemical exposure or are hereditary. Over 2000 Australians die from skin cancer each year.</p>
    <div class="photo-frame"></div>
    <div class="photo-couple" role="img" aria-label="Photo of a smiling older couple embracing outdoors"></div>
    <div class="dot" style="left:299px;top:356px;width:40px;height:40px;background:rgba(201,70,12,.6)"></div>
    <div class="callout">Have you<br>had your<br>skin checked<br>lately?</div>
    <h3 class="contact-title">Contact Us</h3>
    <ul class="contact-list">
      <li><svg viewBox="0 0 16 16"><path d="M8 1a5 5 0 0 0-5 5c0 4 5 9 5 9s5-5 5-9a5 5 0 0 0-5-5zm0 7a2 2 0 1 1 0-4 2 2 0 0 1 0 4z" fill="#e3792b"/></svg>Suite 3 &amp; 4, 118 Harbour Road</li>
      <li class="indent">Seabrook, NSW 2299</li>
      <li><svg viewBox="0 0 16 16"><path d="M3 1.5l3 .5 1 3-1.8 1.3a8 8 0 0 0 4.5 4.5L11 9l3 1 .5 3-2 1.5C6.5 14 2 9.5 1.5 3.5z" fill="#e3792b"/></svg>1300 555 018</li>
      <li><svg viewBox="0 0 16 16"><path d="M3 1.5l3 .5 1 3-1.8 1.3a8 8 0 0 0 4.5 4.5L11 9l3 1 .5 3-2 1.5C6.5 14 2 9.5 1.5 3.5z" fill="#e3792b"/></svg>4300 5561 | FAX</li>
      <li><svg viewBox="0 0 16 16"><rect x="1" y="3.5" width="14" height="9" fill="#e3792b"/><path d="M1 3.5l7 5 7-5" fill="none" stroke="#f6bd55" stroke-width="1.2"/></svg>admin@lumorava.clinic</li>
      <li><svg viewBox="0 0 16 16"><g fill="none" stroke="#e3792b" stroke-width="1.2"><circle cx="8" cy="8" r="6.5"/><ellipse cx="8" cy="8" rx="3" ry="6.5"/><path d="M1.5 8h13M2.5 5h11M2.5 11h11"/></g></svg>www.Lumorava.clinic</li>
    </ul>
  </section>

  <section class="panel panel-cover">
    <div class="cover-photo" role="img" aria-label="Photo of a sunset over a calm beach with wet sand and pebbles"></div>
    <div class="cover-logo">Lumorava</div>
    <p class="cover-tagline">Comfort<br>In Your Skin</p>
  </section>

</div>
</body>
</html>
```